Technology management company looking for a new website with a professional look

Brennick IT is a recently re-branded technology management company that is looking for a website design to match its personalized approach and friendly culture.

We would like to see a specialized, but related, page style for each of our main service offerings of:

• Commercial IT Support (This is our primary focus)
• Commercial Phone Systems (We partner with http://www.voxtrell.com/ for our phone systems)
• Point of Sale Systems (We partner with http://www.tillmora.com/ for our POS systems.
• Web Design
• Hollow Pine Computers (Our residential computer service offering, branded as Hollow Pine Computers)

The Hollow Pine Computers page should be build upon the Hollow Pine Computers logo, the other four pages should be branded as Brennick IT.

These five separate pages should have subtle, yet clearly defined links to one another. They should also each have a Home, Products, Service, and Company in the menu.

The website should have a clean design with professional appeal, but not appear too sterile or uninviting. It needs to have a simple, easy to navigate menu interface along the top. We would also like the site to be mobile friendly.

It should also allow us to easily tie in links to our social media pages (Facebook, LinkedIn, Twitter and Google+) and provide easy access to our contact information from each page.

This is a link to our old website www.hollowpinecomputers.com

We don't currently have copy available. The text and menu design should be easily editable and expandable so we can use the design to fit our copy.

In general we are looking for a concept we can modify to fit our needs.

We need this design to be available with layers in a .psd format.

Target Market(s)

Small to mid-size businesses.

Industry/Entity Type

Information Technology

Number of Pages Required

5+ page

Font styles to use
Sans Serif

Requirements
Must have
• Mobile Friendly
• Professional Type Face
• Unity between all pages
• .PSD Format
Nice to have
• Themed with our logo
Should not have
• Bubbly unprofessional typeface. No comic sans.

```html
<!DOCTYPE html>
<html lang="en">
<head>
<meta charset="utf-8">
<title>Brennick IT — Making Your Technology Work For You</title>
<link href="https://fonts.googleapis.com/css2?family=Open+Sans:ital,wght@0,400;0,600;0,700;0,800;1,400&display=swap" rel="stylesheet">
<style>
:root{
  --blue:#1d5ea8;
  --blue-dark:#164a86;
  --orange:#f47a20;
  --ink:#2a2d33;
  --text:#5b6068;
  --light:#f1f2f4;
  --footer:#2c2e33;
  --footer-line:#44474d;
  --white:#ffffff;
}
*{box-sizing:border-box;margin:0;padding:0}
html,body{width:1200px;height:2912px;overflow:hidden}
body{font-family:"Open Sans",Arial,sans-serif;color:var(--text);background:var(--white);position:relative}
section,header,footer{position:relative;width:1200px;overflow:hidden}

/* Hero */
.hero{height:600px}
.hero-photo{position:absolute;inset:0;background:linear-gradient(100deg,#6b5f58 0%,#a89486 35%,#d9cbbd 60%,#8f8078 100%)}
.hero-shade{position:absolute;inset:0;background:linear-gradient(180deg,rgba(20,22,28,.55) 0%,rgba(20,22,28,.15) 40%,rgba(20,22,28,.35) 100%)}
.topbar{position:absolute;top:0;left:0;right:0;height:80px;background:rgba(22,25,32,.7);display:flex;align-items:center;justify-content:space-between;padding:0 70px 0 60px}
.brand{display:flex;align-items:center;gap:12px;color:var(--white);font-weight:700;font-size:28px}
.brand-mark{width:30px;height:30px;background:var(--white);border-radius:50%}
.nav{display:flex;height:80px}
.nav a{display:flex;align-items:center;padding:0 26px;color:var(--white);text-decoration:none;font-size:13px;font-weight:600;letter-spacing:1px}
.nav a.active{background:var(--blue)}
.hero-copy{position:absolute;left:100px;top:380px;color:var(--white)}
.hero-copy .line{font-size:40px;font-weight:700;line-height:1.1}
.hero-copy .line.indent{padding-left:150px}
.hero-copy .focus{font-size:78px;font-weight:800;color:var(--orange);line-height:1}
.portal{position:absolute;left:800px;top:100px;width:380px;height:280px;background:rgba(10,12,16,.82);padding:28px 30px;color:var(--white)}
.portal h2{font-size:22px;font-weight:700;letter-spacing:.5px}
.portal p{font-size:13px;font-style:italic;margin-top:10px;line-height:1.5;color:#e4e4e4}
.portal .field{margin-top:22px;height:38px;background:var(--white);border-radius:2px}
.portal .terms{display:flex;align-items:center;justify-content:space-between;margin-top:20px;font-size:12px}
.portal .terms span{display:flex;align-items:center;gap:8px}
.portal .box{width:12px;height:12px;border:1px solid #ccc;background:var(--white)}
.portal .signup{background:var(--white);color:var(--ink);font-size:12px;font-weight:700;padding:9px 24px;border-radius:20px}

/* Welcome */
.welcome{height:540px;background:var(--light)}
.welcome-head{background:var(--white);height:120px;padding:46px 100px 0}
.welcome-head h2{font-size:28px;font-weight:800;color:var(--ink)}
.welcome-head .rule{margin-top:18px;height:3px;background:var(--blue)}
.welcome-body{display:flex;gap:60px;padding:40px 100px 0}
.welcome-photo{width:480px;height:320px;background:linear-gradient(135deg,#e8e2da,#b9aea4 60%,#8d8a8a)}
.who{width:460px;padding-top:10px}
.who h3{font-size:30px;font-weight:800;color:var(--ink)}
.who p{font-size:14px;line-height:1.75;margin-top:14px}
.btn-outline{display:inline-block;margin-top:26px;border:2px solid var(--blue);color:var(--ink);font-size:12px;font-weight:700;padding:9px 22px;border-radius:22px}

/* Services */
.services{height:500px}
.services-photo{position:absolute;inset:0;background:linear-gradient(120deg,#2a1b15,#5a3826 45%,#3a2419 75%,#1e1512)}
.services-shade{position:absolute;inset:0;background:rgba(10,8,8,.45)}
.services h2{position:relative;text-align:center;color:var(--white);font-size:36px;font-weight:700;padding-top:36px}
.service-cols{position:relative;display:flex;justify-content:center;gap:200px;margin-top:40px}
.service{width:380px;text-align:center;color:var(--white)}
.service svg{display:block;margin:0 auto}
.service h3{font-size:28px;font-weight:700;margin-top:14px}
.service p{font-size:14px;line-height:1.55;margin-top:10px;color:#e8e8e8}
.btn-solid{display:inline-block;margin-top:20px;background:var(--white);color:var(--ink);font-size:12px;font-weight:700;padding:8px 22px}

/* Products */
.products{height:420px;background:var(--white)}
.products h2,.team h2{text-align:center;color:var(--ink);font-size:36px;font-weight:700;padding-top:40px}
.product-row{position:absolute;left:80px;top:132px;width:1040px;display:flex;gap:40px}
.product{width:230px;height:216px;background:var(--white);box-shadow:0 2px 10px rgba(0,0,0,.12);padding:14px 14px 0;text-align:center}
.product .thumb{height:140px}
.product h3{font-size:16px;font-weight:800;color:var(--ink);margin-top:22px}
.product.featured{background:var(--blue);box-shadow:none;height:236px;margin-top:-10px}
.product.featured .thumb{border:4px solid var(--white)}
.product.featured h3{color:var(--white)}
.arrow{position:absolute;width:44px;height:64px;background:var(--blue);display:flex;align-items:center;justify-content:center}

/* Team */
.team{height:360px;background:linear-gradient(180deg,#ffffff 0%,#eceef1 100%)}
.team-strip{position:absolute;left:100px;top:132px;width:1000px;height:208px;display:flex}
.team-strip .member{flex:1;background:linear-gradient(180deg,#d9d4cf,#a7a19c)}
.team-strip .member:nth-child(2n){background:linear-gradient(180deg,#cfcac6,#958f8b)}
.team-strip .member.lead{background:linear-gradient(180deg,#e5e0db,#b5ada6)}
.team-badge{position:absolute;left:574px;top:300px;width:52px;height:52px;border-radius:50%;background:var(--blue-dark);color:var(--white);font-size:10px;font-weight:700;display:flex;align-items:center;justify-content:center}

/* Footer */
.site-footer{height:492px;background:var(--footer);padding:42px 100px 0}
.footer-cols{display:flex;gap:0}
.footer-col{width:255px;padding-right:30px}
.footer-col:last-child{width:240px;padding-right:0}
.footer-col h4{font-size:22px;font-weight:700;color:var(--white)}
.footer-col .rule{height:1px;background:var(--footer-line);margin:14px 0 18px}
.footer-col p,.footer-col li{font-size:11.5px;line-height:1.7;color:#a9adb3}
.footer-col ul{list-style:none}
.footer-col li{padding-left:12px;position:relative;margin-bottom:5px}
.footer-col li::before{content:"";position:absolute;left:0;top:8px;width:4px;height:4px;background:#a9adb3;border-radius:50%}
.tweet{margin-bottom:14px}
.tweet .when{display:block;color:#7c8188}
.form-field{height:30px;border:1px solid var(--footer-line);background:#25272b;font-size:11px;color:#8d9197;padding:7px 10px;margin-bottom:10px}
.form-field.message{height:70px}
.submit{display:inline-block;background:var(--white);color:var(--ink);font-size:10px;font-weight:700;padding:6px 16px}
.copyright{position:absolute;left:100px;bottom:28px;font-size:11px;color:#7c8188}
</style>
</head>
<body>

<header class="hero">
  <div class="hero-photo" role="img" aria-label="Photo of colleagues working together at laptops in a bright office"></div>
  <div class="hero-shade"></div>
  <div class="topbar">
    <div class="brand"><span class="brand-mark"></span>Brennick IT</div>
    <nav class="nav">
      <a class="active">HOME</a>
      <a>SERVICES</a>
      <a>PRODUCTS</a>
      <a>COMPANY</a>
    </nav>
  </div>
  <div class="hero-copy">
    <div class="line">Making Your</div>
    <div class="focus">TECHNOLOGY</div>
    <div class="line indent">Work For You</div>
  </div>
  <div class="portal">
    <h2>USER PORTAL</h2>
    <p>Sign up to be the first to get all of our best business advice for free to your inbox.</p>
    <div class="field"></div>
    <div class="terms">
      <span><i class="box"></i>Accept All Terms</span>
      <span class="signup">SIGN UP</span>
    </div>
  </div>
</header>

<section class="welcome">
  <div class="welcome-head">
    <h2>WELCOME TO BRENNICK IT</h2>
    <div class="rule"></div>
  </div>
  <div class="welcome-body">
    <div class="welcome-photo" role="img" aria-label="Photo of hands typing on a laptop at a desk"></div>
    <div class="who">
      <h3>WHO WE ARE?</h3>
      <p>We are a friendly technology management team helping small and mid-size businesses run smoothly. From daily support to long-term planning, we look after your systems so you can focus on your customers. Our people take a personal approach, learning how your business works and shaping every solution around it. We keep networks secure, devices updated and staff confident with the tools they use every day, with clear advice and quick answers whenever you need them.</p>
      <span class="btn-outline">READ MORE</span>
    </div>
  </div>
</section>

<section class="services">
  <div class="services-photo" role="img" aria-label="Photo of server rack cabling in warm light"></div>
  <div class="services-shade"></div>
  <h2>Our Services</h2>
  <div class="service-cols">
    <div class="service">
      <svg width="72" height="72" viewBox="0 0 72 72" fill="none" stroke="#fff" stroke-width="3">
        <rect x="10" y="24" width="26" height="42"/><rect x="36" y="8" width="26" height="58"/>
        <path d="M16 32h6M26 32h4M16 42h6M26 42h4M16 52h6M26 52h4M42 16h6M52 16h4M42 26h6M52 26h4M42 36h6M52 36h4M42 46h6M52 46h4M45 66v-10h8v10"/>
      </svg>
      <h3>Residencial</h3>
      <p>Sometimes it's tough to keep home computers, printers and networks working together. We set up, repair and protect the devices your family relies on, so everything simply works when you need it.</p>
      <span class="btn-solid">READ MORE</span>
    </div>
    <div class="service">
      <svg width="72" height="72" viewBox="0 0 72 72" fill="none" stroke="#fff" stroke-width="3">
        <rect x="10" y="44" width="10" height="22"/><rect x="26" y="34" width="10" height="32"/><rect x="42" y="24" width="10" height="42"/>
        <path d="M8 30 L30 14 L42 20 L62 6 M54 6h8v8"/><path d="M4 66h64"/>
      </svg>
      <h3>Commercial</h3>
      <p>We offer a wide variety of services for our commercial clients, depending on the scope of their business and their needs. Click the button below to learn more detailed information on each of our offers.</p>
      <span class="btn-solid">READ MORE</span>
    </div>
  </div>
</section>

<section class="products">
  <h2>Our Products</h2>
  <div class="product-row">
    <div class="product">
      <div class="thumb" role="img" aria-label="Photo of a consultant reviewing a report" style="background:linear-gradient(135deg,#e9d9b8,#c2a77a)"></div>
      <h3>SURVEY &amp; ANALYSIS</h3>
    </div>
    <div class="product">
      <div class="thumb" role="img" aria-label="Photo of hands sketching a network plan" style="background:linear-gradient(135deg,#ece6dd,#b6aa9a)"></div>
      <h3>DESIGN &amp; PLOT</h3>
    </div>
    <div class="product featured">
      <div class="thumb" role="img" aria-label="Illustration of connected network devices" style="background:linear-gradient(135deg,#e6eef6,#8fb0d3)"></div>
      <h3>STAGE &amp; CONFIGURE</h3>
    </div>
    <div class="product">
      <div class="thumb" role="img" aria-label="Photo of a phone and tablet on a desk" style="background:linear-gradient(135deg,#d8dde2,#7d8791)"></div>
      <h3>INSTALL &amp; REMEDIATE</h3>
    </div>
  </div>
  <div class="arrow" style="left:70px;top:216px"><svg width="16" height="22" viewBox="0 0 16 22"><path d="M12 3 L4 11 L12 19" fill="none" stroke="#fff" stroke-width="3"/></svg></div>
  <div class="arrow" style="left:1086px;top:216px"><svg width="16" height="22" viewBox="0 0 16 22"><path d="M4 3 L12 11 L4 19" fill="none" stroke="#fff" stroke-width="3"/></svg></div>
</section>

<section class="team">
  <h2>Our Professional Team</h2>
  <div class="team-strip" role="img" aria-label="Row of portrait photos of team members">
    <div class="member"></div><div class="member"></div><div class="member"></div>
    <div class="member lead"></div>
    <div class="member"></div><div class="member"></div><div class="member"></div>
  </div>
  <div class="team-badge">EXPERT</div>
  <div class="arrow" style="left:100px;top:204px"><svg width="16" height="22" viewBox="0 0 16 22"><path d="M12 3 L4 11 L12 19" fill="none" stroke="#fff" stroke-width="3"/></svg></div>
  <div class="arrow" style="left:1056px;top:204px"><svg width="16" height="22" viewBox="0 0 16 22"><path d="M4 3 L12 11 L4 19" fill="none" stroke="#fff" stroke-width="3"/></svg></div>
</section>

<footer class="site-footer">
  <div class="footer-cols">
    <div class="footer-col">
      <h4>Contact</h4>
      <div class="rule"></div>
      <p>Brennick IT</p>
      <p style="margin-top:10px">Harbourside Office, Head Office<br>Floor 4, Unit 18, 56 Kestrel Lane,<br>Harbourside 3100</p>
      <p style="margin-top:10px">Phone (03) 9100 2468<br>hello@brennickit.com</p>
      <p style="margin-top:10px">Northfield Office<br>Unit 9, 214 Linden Road,<br>Northfield 3140<br>(03) 9100 8642</p>
    </div>
    <div class="footer-col">
      <h4>Quick Links</h4>
      <div class="rule"></div>
      <ul>
        <li>Commercial IT support</li>
        <li>Home computer service</li>
        <li>Phone systems for offices</li>
        <li>Point of sale systems</li>
        <li>Website design and hosting</li>
        <li>Our team and culture</li>
        <li>Get in touch today</li>
      </ul>
    </div>
    <div class="footer-col">
      <h4>Latest Tweets</h4>
      <div class="rule"></div>
      <p class="tweet">@brennickit Quick tip: keep backups off site and test them every month. <span class="when">1 day ago</span></p>
      <p class="tweet">@brennickit Our new phone system rollout is live for clients across town. <span class="when">2 days ago</span></p>
      <p class="tweet">@brennickit Meet the team at the small business expo next week. <span class="when">3 days ago</span></p>
    </div>
    <div class="footer-col">
      <h4>Contact Us</h4>
      <div class="rule"></div>
      <div class="form-field">First Name</div>
      <div class="form-field">Email Address</div>
      <div class="form-field">Subject</div>
      <div class="form-field message">Message</div>
      <span class="submit">SUBMIT</span>
    </div>
  </div>
  <div class="copyright">Copyright © 2015 Brennick IT - All Rights Reserved</div>
</footer>

</body>
</html>
```